Tamkor, a service provider dedicated to improving the performance of a website

Tamkor offers optimization and performance improvement for all types of websites (showcase sites, e-commerce, ...), with the aim of improving their ranking on Vintrel and their customer transformation rate. The main benefits consist in optimizing the factors of a site. In addition, we also offer content creation (description of product sheets, services, ...), Vintrel Ads campaign management, migration version for Prestashop / Wordpress, etc. The design must be a fresh image, dynamic, why not "fun", but also serious. No favorite color, carte blanche on this point;)

```html
<!DOCTYPE html>
<html lang="en">
<head>
<meta charset="UTF-8">
<title>Tamkor – Business Card</title>
<link rel="stylesheet" href="https://fonts.googleapis.com/css2?family=Raleway:wght@400;500;600;700;800&display=swap">
<style>
  :root {
    --brand-blue: #2f4c9e;
    --brand-blue-dark: #24408a;
    --lavender: #dcdcef;
    --lavender-light: #eeeef8;
    --card-white: #ffffff;
    --stage: #e9e9ee;
  }
  * { margin: 0; padding: 0; box-sizing: border-box; }
  html, body { width: 1200px; height: 800px; overflow: hidden; }
  body {
    background: var(--stage);
    font-family: "Raleway", sans-serif;
    color: var(--brand-blue);
    display: flex;
    align-items: center;
    justify-content: center;
    gap: 40px;
  }
  .card {
    position: relative;
    width: 540px;
    height: 310px;
    background: var(--card-white);
    border-radius: 4px;
    box-shadow: 0 10px 30px rgba(30, 40, 80, 0.15);
    overflow: hidden;
  }

  /* Front */
  .card-front .pattern-field {
    position: absolute;
    inset: 0;
    background: linear-gradient(135deg, var(--lavender-light) 0%, var(--lavender) 50%, var(--lavender-light) 100%);
  }
  .card-front .front-brand {
    position: absolute;
    inset: 0;
    display: flex;
    align-items: center;
    justify-content: center;
    gap: 14px;
  }
  .brand-square {
    width: 58px;
    height: 58px;
    border-radius: 14px;
    background: var(--brand-blue);
  }
  .front-brand .brand-name {
    font-size: 52px;
    font-weight: 800;
    letter-spacing: -1px;
  }

  /* Back */
  .card-back .brand-row {
    position: absolute;
    left: 40px;
    top: 60px;
    display: flex;
    align-items: center;
    gap: 16px;
  }
  .brand-row .brand-square {
    width: 54px;
    height: 54px;
    border-radius: 13px;
  }
  .brand-row .brand-name {
    font-size: 60px;
    font-weight: 800;
    letter-spacing: -1.5px;
    line-height: 1;
  }
  .card-back .divider {
    position: absolute;
    left: 40px;
    right: 36px;
    top: 188px;
    height: 1px;
    background: var(--brand-blue);
  }
  .contact-block {
    position: absolute;
    left: 40px;
    top: 200px;
  }
  .person-name {
    font-size: 17px;
    font-weight: 800;
  }
  .person-role {
    font-size: 12px;
    font-weight: 500;
    margin-bottom: 6px;
  }
  .contact-list { list-style: none; }
  .contact-list li {
    display: flex;
    align-items: center;
    gap: 7px;
    font-size: 12px;
    font-weight: 500;
    line-height: 1.45;
  }
  .contact-list svg { width: 10px; height: 10px; flex: none; }
  .address-block {
    position: absolute;
    right: 36px;
    top: 200px;
    text-align: right;
    font-size: 12px;
    font-weight: 500;
    line-height: 1.45;
  }
</style>
</head>
<body>
  <section class="card card-front" aria-label="Card front">
    <div class="pattern-field" role="img" aria-label="Faint repeated brand-name pattern across the card"></div>
    <div class="front-brand">
      <span class="brand-square"></span>
      <span class="brand-name">Tamkor</span>
    </div>
  </section>

  <section class="card card-back" aria-label="Card back">
    <div class="brand-row">
      <span class="brand-square"></span>
      <span class="brand-name">Tamkor</span>
    </div>
    <div class="divider"></div>
    <div class="contact-block">
      <p class="person-name">Lena Hartwell</p>
      <p class="person-role">Owner</p>
      <ul class="contact-list">
        <li>
          <svg viewBox="0 0 10 10"><rect x="2" y="0.5" width="6" height="9" rx="1" fill="none" stroke="currentColor" stroke-width="1"/></svg>
          0198 765 432
        </li>
        <li>
          <svg viewBox="0 0 10 10"><rect x="0.5" y="2" width="9" height="6.5" fill="currentColor"/><path d="M0.5 2 L5 5.5 L9.5 2" fill="none" stroke="#fff" stroke-width="0.9"/></svg>
          info@tamkormail.com
        </li>
        <li>
          <svg viewBox="0 0 10 10"><circle cx="5" cy="5" r="4.5" fill="currentColor"/><path d="M0.5 5 H9.5 M5 0.5 V9.5 M5 0.5 C2.5 3 2.5 7 5 9.5 M5 0.5 C7.5 3 7.5 7 5 9.5" fill="none" stroke="#fff" stroke-width="0.6"/></svg>
          www.tamkorweb.com
        </li>
      </ul>
    </div>
    <div class="address-block">
      <p>PO BOX 456, Harbour Lane</p>
      <p>2nd street Ashford</p>
    </div>
  </section>
</body>
</html>
```